Website for Company to help with House Restoration from Hurricane Damage

Crisp, Clean and Professional!

I need a FRONT page for a website. I need it created in photoshop with the layers intact. We DO NOT need the HTML or RBT for the site. Simply the design. Any fonts you use will need to be included if they are not standard. Please make sure any fonts you use in the body of the text are available for use on Google Fonts.

I have attached a word doc that lists the menu items and additional instructions.

A little about the company - after Hurricane Quintessa - RBT developed a system which allows the house to be raised, the Pylonets installed, and the house reset on the Pylonets without the expense of moving the house or driving new pilings. This option can be installed in a matter of days with limited space and at a lower construction cost.

Please refer to the attached musthaves.doc and images that are included.

The main page must incorporate the menu, the attached photos w/ text underneath (text is in the word doc attached), and the text included in the word doc.

Standard footer with contact info as well.

If you have questions please contact us!
Updates

Designs are due by Friday! We will pick one this weekend.  We are unable to change it from 10 days to 5.  Thank you!!!

Target Market(s)

People who lost their homes or businesses due to a hurricane.

Industry/Entity Type

Construction

Requirements
Must have
• See attached musthaves.doc

```html
<!DOCTYPE html>
<html lang="en">
<head>
<meta charset="utf-8">
<title>Resilient Base Technologies, LLC (RBT)</title>
<link rel="stylesheet" href="https://fonts.googleapis.com/css2?family=Open+Sans:wght@400;600&family=Playball&display=swap">
<style>
  :root {
    --paper: #f2f2f1;
    --header: #f4f4f3;
    --ink: #4e4e4e;
    --ink-soft: #5a5a5a;
    --nav: #555555;
    --nav-active: #6d8a3a;
    --rule: #6a6a6a;
    --button: #707070;
    --footer: #2b2b2b;
    --footer-box: #3a3a3a;
    --footer-text: #c9c9c9;
    --social-band: #3d3d3d;
    --social-icon: #a9a9a9;
    --caption-dark: rgba(40, 40, 40, 0.82);
    --caption-mid: rgba(110, 110, 110, 0.9);
  }
  * { margin: 0; padding: 0; box-sizing: border-box; }
  html, body { width: 1200px; height: 1173px; overflow: hidden; }
  body {
    position: relative;
    background: var(--paper);
    font-family: "Open Sans", Arial, sans-serif;
    color: var(--ink);
  }
  .site-header {
    position: absolute; left: 0; top: 0; width: 1200px; height: 80px;
    background: var(--header);
    border-bottom: 1px solid #d8d8d8;
  }
  .brand {
    position: absolute; left: 193px; top: 12px; width: 200px;
    display: flex; flex-direction: column; align-items: center;
  }
  .brand-mark {
    width: 26px; height: 26px; border-radius: 50%;
    background: #8fa866;
  }
  .brand-name {
    margin-top: 6px;
    font-size: 12px; font-weight: 600; color: #3f3f3f; letter-spacing: 0.2px;
  }
  .main-nav {
    position: absolute; top: 34px; left: 0; width: 1200px; height: 20px;
    font-size: 12px; color: var(--nav);
  }
  .main-nav span { position: absolute; white-space: nowrap; }
  .main-nav .is-active { color: var(--nav-active); font-weight: 600; }

  .hero {
    position: absolute; left: 0; top: 80px; width: 1200px; height: 379px;
    overflow: hidden;
  }
  .hero-photo {
    position: absolute; inset: 0;
    background: linear-gradient(180deg,
      #d6a0a0 0%, #e9a88c 10%, #c98d86 20%, #7b7a8c 26%,
      #6d7588 40%, #5d6276 60%, #4d4f5c 78%, #3a3836 92%, #2f2c28 100%);
  }
  .hero-arrow { position: absolute; top: 184px; }
  .hero-caption {
    position: absolute; left: 308px; top: 336px; width: 567px; height: 32px;
    border-radius: 16px; background: var(--caption-dark);
    font-family: "Playball", cursive; color: #ffffff; font-size: 19px;
  }
  .hero-caption .pill-mid {
    position: absolute; left: 140px; top: 0; width: 127px; height: 32px;
    border-radius: 16px; background: var(--caption-mid);
  }
  .hero-caption span { position: absolute; top: 3px; white-space: nowrap; }

  .intro {
    position: absolute; left: 253px; top: 505px; width: 694px;
  }
  .intro-title {
    font-family: "Playball", cursive; font-weight: 400;
    font-size: 21px; color: #444; text-align: center;
  }
  .intro-rule {
    position: absolute; left: 28px; top: 42px; width: 636px; height: 1px;
    background: var(--rule);
  }
  .intro-text {
    margin-top: 29px;
    font-size: 11.4px; line-height: 21.1px; color: var(--ink-soft);
  }
  .intro-text p + p { margin-top: 21px; }
  .read-more {
    display: inline-block; margin-left: 12px; padding: 0 9px;
    height: 19px; line-height: 19px; vertical-align: 1px;
    background: var(--button); color: #ffffff; border-radius: 3px;
    font-size: 9.5px; letter-spacing: 0.4px;
  }

  .site-footer {
    position: absolute; left: 0; top: 868px; width: 1200px; height: 230px;
    background: var(--footer);
  }
  .contact-card {
    position: absolute; left: 258px; top: 43px; width: 335px; height: 135px;
    background: var(--footer-box);
  }
  .contact-card h3, .sitemap h3 {
    font-family: "Playball", cursive; font-weight: 400; color: #bdbdbd;
  }
  .contact-card h3 { position: absolute; left: 37px; top: 24px; font-size: 15px; }
  .contact-card address {
    position: absolute; left: 56px; top: 53px;
    font-style: normal; font-size: 11.4px; line-height: 21.5px; color: var(--footer-text);
  }
  .sitemap { position: absolute; left: 738px; top: 43px; }
  .sitemap h3 { font-size: 15px; }
  .sitemap ul {
    list-style: none; margin-top: 5px; margin-left: 7px;
    font-size: 11.4px; line-height: 17px; color: var(--footer-text);
  }
  .sitemap li::before { content: "::"; margin-right: 5px; font-size: 9px; color: #8c8c8c; }

  .social-band {
    position: absolute; left: 0; top: 1098px; width: 1200px; height: 47px;
    background: var(--social-band);
    display: flex; justify-content: center; align-items: center; gap: 23px;
  }
  .social-dot {
    width: 22px; height: 22px; border-radius: 50%; background: var(--social-icon);
  }
  .base-strip {
    position: absolute; left: 0; top: 1145px; width: 1200px; height: 28px;
    background: var(--footer);
  }
</style>
</head>
<body>
  <header class="site-header">
    <div class="brand">
      <div class="brand-mark"></div>
      <div class="brand-name">Resilient Base Technologies</div>
    </div>
    <nav class="main-nav">
      <span class="is-active" style="left:441px">Home</span>
      <span style="left:502px">Services</span>
      <span style="left:579px">About us</span>
      <span style="left:657px">Product Specifications</span>
      <span style="left:810px">Design Documentation</span>
      <span style="left:955px">Contact Us</span>
    </nav>
  </header>

  <section class="hero">
    <div class="hero-photo" role="img" aria-label="Sunset over a calm bay with moored boats; a parent crouches on the beach holding hands with a small child, both in silhouette"></div>
    <svg class="hero-arrow" style="left:129px" width="20" height="30" viewBox="0 0 20 30"><path d="M17 2 L4 15 L17 28" fill="none" stroke="#ffffff" stroke-width="2.4"/></svg>
    <svg class="hero-arrow" style="left:1045px" width="20" height="30" viewBox="0 0 20 30"><path d="M3 2 L16 15 L3 28" fill="none" stroke="#ffffff" stroke-width="2.4"/></svg>
    <div class="hero-caption">
      <div class="pill-mid"></div>
      <span style="left:14px">Rebuild Safer</span>
      <span style="left:178px">Stronger</span>
      <span style="left:281px">Better to build new lasting memories</span>
    </div>
  </section>

  <main class="intro">
    <h1 class="intro-title">Resilient Base Technologies, LLC (RBT)</h1>
    <div class="intro-rule"></div>
    <div class="intro-text">
      <p>Systems for extending the height of existing piles are not available on today’s market.&nbsp; Resilient Base Technologies, LLC (RBT) has developed two systems to allow for Piles to be extended that provide superior structural support without corrosion and maintenance concerns.&nbsp; We provided two systems, a complete system, Pile Cap Extension Pylonets, and Pile Splice.&nbsp; These two systems allow a home to be raised to by up to 54”, higher extensions possible with additional design consideration for lateral support. Shown below is the full Piling Extension system, which connects to the top of the existing pile. The system modular and can be cut to meet specific needs of the home.</p>
      <p>Our Patented Piling system has been designed to withstand the corrosive environment of beach communities. The salt water and wind-blown sand corrodes unprotected materials, and yes, even stainless steel. Our system utilizes a high strength carbon fiber material that is corrosion proof from salt water and UV proof.&nbsp; The system will not erode, decay or loose strength over time. The system has three installation conditions, for raising a house on existing pilings, repairing damaged pilings, and for connecting new pilings to floor joists in new construction. The three options are generally described here. <span class="read-more">READ MORE &gt;&gt;</span></p>
    </div>
  </main>

  <footer class="site-footer">
    <div class="contact-card">
      <h3>Resilient Base Technologies, LLC (RBT)</h3>
      <address>
        P.O. Box : 41825,&nbsp; Cedar Hollow,<br>
        PA : 19014-0330 - (555) 014-2280<br>
        Email : sales@resilientbasetech.com
      </address>
    </div>
    <div class="sitemap">
      <h3>Site Map</h3>
      <ul>
        <li>Home</li>
        <li>Services</li>
        <li>About Us</li>
        <li>Product Specifications</li>
        <li>Design Documentation</li>
        <li>Contact Us</li>
      </ul>
    </div>
  </footer>

  <div class="social-band">
    <span class="social-dot"></span>
    <span class="social-dot"></span>
    <span class="social-dot"></span>
    <span class="social-dot"></span>
    <span class="social-dot"></span>
    <span class="social-dot"></span>
    <span class="social-dot"></span>
    <span class="social-dot"></span>
  </div>
  <div class="base-strip"></div>
</body>
</html>
```